Bramwell Health Promotional flyer

Develop a professional flyer to be distributed to potential clients for consulting services.
Company name: Bramwell Health
see attachments for company logo and other bullet points . Bold items need to be on the flyer as written, other items can be tweaked/updated to sound more appealing.

```html
<!DOCTYPE html>
<html lang="en">
<head>
<meta charset="utf-8">
<title>Bramwell Health – Consulting Services Flyer</title>
<link rel="stylesheet" href="https://fonts.googleapis.com/css2?family=Lato:ital,wght@0,400;0,700;0,900;1,400&family=Tinos&display=swap">
<style>
:root{
  --page-bg:#d7d7d7;
  --paper:#ffffff;
  --blue:#1f5cb8;
  --blue-deep:#184a99;
  --charcoal:#4a4a4a;
  --grey-band:#6b6b6b;
  --grey-band-light:#a3a3a3;
  --ink:#3a3a3a;
  --white:#ffffff;
}
*{box-sizing:border-box;margin:0;padding:0}
html,body{width:1200px;height:1177px;overflow:hidden;background:var(--page-bg)}
body{font-family:"Lato",sans-serif;color:var(--ink)}
h2{font-weight:400}
.flyer{position:absolute;left:217px;top:93px;width:766px;height:990px;background:var(--paper);overflow:hidden}

.hero-shape{position:absolute;left:0;top:0;width:766px;height:408px}
.logo-badge{position:absolute;left:30px;top:18px;width:228px;height:228px;border-radius:50%;background:var(--white);border:6px solid var(--blue);box-shadow:6px 8px 0 rgba(0,0,0,.18);display:flex;align-items:center;justify-content:center;text-align:center}
.logo-name{font-family:"Lato",sans-serif;font-weight:900;color:var(--blue);font-size:27px;line-height:1.1;letter-spacing:.5px}

.services-title{position:absolute;left:332px;top:56px;width:344px;height:47px;border:1.5px solid var(--white);color:var(--white);font-family:"Tinos",serif;font-size:30px;letter-spacing:6px;display:flex;align-items:center;justify-content:center}
.services-list{position:absolute;left:326px;top:121px;width:420px;list-style:none;color:var(--white);font-size:14.4px;line-height:17.5px}
.services-list li{padding-left:11px;position:relative}
.services-list li::before{content:"";position:absolute;left:0;top:7px;width:5px;height:5px;border-radius:50%;background:var(--white)}
.services-note{position:absolute;left:337px;top:316px;width:400px;color:var(--white);font-style:italic;font-size:14.4px;line-height:17.5px}

.why-title{position:absolute;left:24px;top:339px;font-family:"Tinos",serif;font-size:24px;line-height:24px;color:var(--charcoal)}
.why-title .brand{color:var(--blue);display:block}

.benefit{position:absolute;top:490px;width:169px;height:136px;color:var(--white);font-weight:900;font-size:14.5px;line-height:17px;text-transform:uppercase;text-align:center;display:flex;align-items:flex-end;justify-content:center;padding:0 10px 18px}
.benefit--blue{background:var(--blue)}
.benefit--grey{background:var(--charcoal)}
.benefit--small{font-size:12.5px;line-height:15px;padding-bottom:12px}
.benefit-icon{position:absolute;top:432px;width:96px;height:96px;border-radius:50%;background:var(--white);border:4px solid;display:flex;align-items:center;justify-content:center}
.benefit-icon--blue{border-color:var(--blue)}
.benefit-icon--grey{border-color:var(--charcoal)}
.icon-credit{position:absolute;left:32px;top:632px;font-size:9.5px;font-weight:700;color:var(--charcoal)}

.bio-band{position:absolute;left:0;top:706px;width:766px;height:224px;background:linear-gradient(90deg,var(--grey-band) 0%,#7d7d7d 55%,var(--grey-band-light) 100%)}
.bio-tab{position:absolute;left:0;top:662px;width:380px;height:44px}
.bio-title{position:absolute;left:30px;top:667px;font-family:"Tinos",serif;font-size:27px;line-height:34px;color:var(--white);letter-spacing:.5px;white-space:nowrap}
.bio-text{position:absolute;left:30px;top:742px;width:454px;font-size:13.2px;line-height:17.5px;color:var(--white);text-align:justify}
.portrait{position:absolute;left:528px;top:668px;width:210px;height:262px;background:radial-gradient(ellipse at 50% 35%,#d9d4cf 0%,#b8b3ae 40%,#9c9c9c 75%,transparent 100%)}

.footer-item{position:absolute;top:947px;display:flex;align-items:center;gap:10px;font-size:16px;color:var(--ink);white-space:nowrap}
.footer-icon{width:34px;height:34px;border-radius:50%;border:2.5px solid var(--blue);display:flex;align-items:center;justify-content:center}
.phone-block{position:absolute;left:478px;top:935px;width:288px;height:55px}
.phone-number{position:absolute;left:556px;top:944px;font-size:25px;color:var(--white);letter-spacing:.5px}
</style>
</head>
<body>
<main class="flyer">

  <svg class="hero-shape" viewBox="0 0 766 408" aria-hidden="true">
    <defs>
      <linearGradient id="heroFill" x1="0" y1="0" x2="1" y2="1">
        <stop offset="0" stop-color="#1f5cb8"/>
        <stop offset=".55" stop-color="#2a66bf"/>
        <stop offset="1" stop-color="#1a4fa3"/>
      </linearGradient>
    </defs>
    <polygon points="84,0 766,0 766,408 242,408" fill="url(#heroFill)"/>
    <polygon points="84,0 112,0 258,408 242,408" fill="#184a99"/>
  </svg>
  <div role="img" aria-label="Soft blurred photo of a clinic interior behind the services list" style="position:absolute;left:340px;top:0;width:426px;height:408px;background:radial-gradient(ellipse at 40% 65%,rgba(120,160,220,.35),transparent 70%)"></div>

  <div class="logo-badge"><span class="logo-name">BRAMWELL<br>HEALTH</span></div>

  <h2 class="services-title">SERVICES</h2>
  <ul class="services-list">
    <li>Retention of Emergency Medicine trained physician, Dr. Thomas E. Whitcombe MD for consultation on work-related injuries, illnesses or testing requirements.</li>
    <li>Assist with occupational health risk management.</li>
    <li>Concierge level service and care at one of Dr. Whitcombe's 4 urgent care clinics when needed.</li>
    <li>Assistance setting up onsite clinics/ medics.</li>
    <li>Access to onsite services such as flu/covid vaccination clinics, onsite drug and alcohol testing, educational sessions, etc.</li>
  </ul>
  <p class="services-note">Job sites do not need to be in Ohio for Dr. Whitcombe to provide consultative services.</p>

  <h2 class="why-title">WHY RETAIN<span class="brand">BRAMWELL<br>HEALTH</span></h2>

  <div class="benefit benefit--blue" style="left:25px">24/7 access<br>to a medical<br>director</div>
  <div class="benefit benefit--grey" style="left:208px">Reduction in<br>recordable<br>work-related<br>injuries</div>
  <div class="benefit benefit--blue" style="left:389px">Concierge level<br>service for your<br>employees and<br>managers</div>
  <div class="benefit benefit--grey benefit--small" style="left:570px">Access to Bramwell<br>Health's referral<br>network of imaging<br>and orthopedics<br>and other providers</div>

  <div class="benefit-icon benefit-icon--blue" style="left:62px">
    <svg width="58" height="58" viewBox="0 0 58 58" fill="none" stroke="#1f5cb8" stroke-width="2.5">
      <path d="M10 22a20 20 0 0 1 36-6"/><path d="M46 8v9h-9"/>
      <path d="M48 36a20 20 0 0 1-36 6"/><path d="M12 50v-9h9"/>
      <text x="29" y="35" font-family="Lato,sans-serif" font-size="16" font-weight="900" fill="#1f5cb8" stroke="none" text-anchor="middle">24/7</text>
    </svg>
  </div>
  <div class="benefit-icon benefit-icon--grey" style="left:245px">
    <svg width="56" height="56" viewBox="0 0 56 56" fill="none" stroke="#4a4a4a" stroke-width="2.5">
      <circle cx="28" cy="17" r="9"/><path d="M19 14h18"/>
      <path d="M10 52v-10a10 10 0 0 1 10-10h16a10 10 0 0 1 10 10v10z"/><path d="M20 33l16 19"/>
    </svg>
  </div>
  <div class="benefit-icon benefit-icon--blue" style="left:426px">
    <svg width="60" height="56" viewBox="0 0 60 56" fill="none" stroke="#1f5cb8" stroke-width="2.5">
      <path d="M30 4l2.5 5 5.5.8-4 3.8 1 5.4-5-2.6-5 2.6 1-5.4-4-3.8 5.5-.8z"/>
      <circle cx="30" cy="28" r="5"/><circle cx="15" cy="32" r="5"/><circle cx="45" cy="32" r="5"/>
      <path d="M21 50v-7a9 9 0 0 1 18 0v7z"/><path d="M6 52v-6a8 8 0 0 1 14-5"/><path d="M54 52v-6a8 8 0 0 0-14-5"/>
    </svg>
  </div>
  <div class="benefit-icon benefit-icon--grey" style="left:607px">
    <svg width="58" height="56" viewBox="0 0 58 56" fill="none" stroke="#4a4a4a" stroke-width="2.5">
      <circle cx="40" cy="12" r="8"/><circle cx="14" cy="28" r="8"/><circle cx="40" cy="44" r="8"/>
      <path d="M21 24l12-8M21 32l12 8"/>
    </svg>
  </div>

  <p class="icon-credit">Icons by Linework from Iconshelf.com</p>

  <div class="bio-band"></div>
  <svg class="bio-tab" viewBox="0 0 380 44" aria-hidden="true">
    <polygon points="0,0 357,0 343,44 0,44" fill="#1f5cb8"/>
    <polygon points="361,0 373,0 359,44 347,44" fill="#4a4a4a"/>
  </svg>
  <h2 class="bio-title">DR. WHITCOMBE BIO</h2>
  <p class="bio-text">Dr. Whitcombe grew up in Westbrook Heights, Ohio and graduated from Linden Preparatory High School, Central Plains University and Harrow Medical College. Dr. Whitcombe is Board Certified as a Diplomate of the National Board of Acute Care Practice and is a Fellow in the National Academy of Acute Care Practice. He practiced Emergency Medicine for 17 years at Ridgeway Medical Center in Millbrook Ohio. Dr. Whitcombe has practiced Urgent Care and Occupational Health Medicine for the last 29 years. He and his wife of 39 years have 3 children and live in Westbrook Heights, Ohio.</p>
  <div class="portrait" role="img" aria-label="Photo of Dr. Whitcombe in a white coat with a stethoscope"></div>

  <div class="footer-item" style="left:28px">
    <span class="footer-icon">
      <svg width="16" height="18" viewBox="0 0 16 18"><path d="M8 1a6 6 0 0 1 6 6c0 4.5-6 10-6 10S2 11.5 2 7a6 6 0 0 1 6-6z" fill="#1f5cb8"/><circle cx="8" cy="7" r="2.3" fill="#fff"/></svg>
    </span>address, ZIP, City
  </div>
  <div class="footer-item" style="left:238px">
    <span class="footer-icon">
      <svg width="18" height="14" viewBox="0 0 18 14"><rect x="0.5" y="0.5" width="17" height="13" rx="1.5" fill="#1f5cb8"/><path d="M1.5 2l7.5 6 7.5-6" stroke="#fff" stroke-width="1.5" fill="none"/></svg>
    </span>whitcombe@email.com
  </div>
  <svg class="phone-block" viewBox="0 0 288 55" aria-hidden="true">
    <polygon points="20,0 62,0 46,55 0,55" fill="#1f5cb8"/>
    <polygon points="70,0 288,0 288,55 54,55" fill="#4a4a4a"/>
    <path d="M22 18c2-2 4-2 5 0l2 3c1 1.5 0 2.5-1 3.5 1 2.5 3 4.5 5.5 5.5 1-1 2-2 3.5-1l3 2c2 1 2 3 0 5-3 3-8 1-13-4s-7-10-5-14z" fill="#fff"/>
  </svg>
  <span class="phone-number">555014267</span>
</main>
</body>
</html>
```